Design for a pull up banner 2100mm x 810mm

A business pull up banner incorporating the business logo, photograph of our trainer and the key benefits of our training courses
please look at home page www.brightmolarclinic.com
'climb your ladder to success'
with you every step of the way

Target Market(s)

course delegates, dentists

Industry/Entity Type

Business

Requirements
Must have
• professional look
• benefits of BMC
• 'climb your ladder to success'
• with you every step of the way
• Selling with integrity
• Increasing profits
• Transforming relationships
• Improving communication
• Growing in confidence
• Changing patients perceptions
Nice to have
• i'd like to see an example with his photo on and without, focusing on the ladder to success (see logo)

```html
<!DOCTYPE html>
<html lang="en">
<head>
<meta charset="utf-8">
<title>Bright Molar Clinic – Pull Up Banner</title>
<link rel="stylesheet" href="https://fonts.googleapis.com/css2?family=Barlow+Condensed:wght@500&family=Questrial&display=swap">
<style>
  :root {
    --ink: #111111;
    --paper: #ffffff;
    --panel: #0d0d0d;
    --yellow: #ffe000;
    --amber: #f7a600;
    --orange: #f07a10;
    --red: #e5321b;
    --text-light: #e9e9e9;
    --photo-light: #6a6a6a;
    --photo-dark: #141414;
  }
  * { box-sizing: border-box; margin: 0; padding: 0; }
  html, body {
    width: 1200px;
    height: 2397px;
    overflow: hidden;
    background: var(--panel);
  }
  .banner {
    position: relative;
    width: 1200px;
    height: 2397px;
    background: var(--panel);
    font-family: "Questrial", "Helvetica Neue", Arial, sans-serif;
  }
  .banner__header {
    position: absolute;
    left: 0; top: 0;
    width: 1200px;
    height: 520px;
    background: var(--paper);
  }
  .brand-name {
    position: absolute;
    left: 90px; top: 110px;
    width: 1040px;
    color: var(--ink);
    font-size: 124px;
    line-height: 1.04;
    letter-spacing: 4px;
    text-transform: uppercase;
    font-weight: 400;
    white-space: nowrap;
  }
  .brand-name span { display: block; }
  .brand-name .line-1 { padding-left: 260px; }
  .brand-name .line-2 { padding-left: 0; }
  .brand-name .line-3 { padding-left: 410px; }
  .accent-rule {
    position: absolute;
    left: 0; top: 520px;
    width: 1200px;
    height: 12px;
    background: linear-gradient(90deg, var(--yellow), var(--amber) 45%, var(--orange) 75%, var(--red));
  }
  .trainer-photo {
    position: absolute;
    left: 0; top: 532px;
    width: 1200px;
    height: 820px;
    background: radial-gradient(ellipse at 40% 35%, var(--photo-light) 0%, #3a3a3a 40%, var(--photo-dark) 85%);
  }
  .benefits {
    position: absolute;
    left: 80px; top: 1400px;
    width: 1060px;
  }
  .headline {
    font-family: "Barlow Condensed", "Arial Narrow", sans-serif;
    font-weight: 500;
    font-size: 80px;
    line-height: 1.05;
    text-transform: uppercase;
    white-space: nowrap;
    background: linear-gradient(90deg, var(--yellow), var(--amber) 60%, var(--orange));
    -webkit-background-clip: text;
    background-clip: text;
    color: transparent;
  }
  .headline span { display: block; }
  .benefit-list {
    list-style: none;
    margin-top: 40px;
  }
  .benefit-list li {
    display: flex;
    align-items: center;
    gap: 26px;
    color: var(--text-light);
    font-size: 44px;
    letter-spacing: 1px;
    text-transform: uppercase;
    height: 88px;
    white-space: nowrap;
  }
  .benefit-list svg { flex: none; width: 40px; height: 40px; }
  .web-band {
    position: absolute;
    left: 0; top: 2140px;
    width: 1200px;
    height: 100px;
    display: flex;
    align-items: center;
    gap: 22px;
    padding-left: 80px;
    background: linear-gradient(90deg, var(--yellow), var(--amber) 40%, var(--orange) 75%, var(--red));
    color: var(--ink);
    font-size: 58px;
    white-space: nowrap;
  }
  .web-band svg { width: 46px; height: 46px; flex: none; }
</style>
</head>
<body>
<main class="banner">
  <header class="banner__header">
    <h1 class="brand-name">
      <span class="line-1">Bright</span>
      <span class="line-2">Molar Clinic</span>
      <span class="line-3">Training</span>
    </h1>
  </header>
  <div class="accent-rule"></div>

  <div class="trainer-photo" role="img" aria-label="Black and white photograph of the trainer in a pinstripe suit adjusting his shirt cuff"></div>

  <section class="benefits">
    <h2 class="headline"><span>Climb your ladder to success</span><span>with you every step of the way</span></h2>
    <ul class="benefit-list">
      <li><svg viewBox="0 0 40 40" aria-hidden="true"><rect x="3" y="3" width="34" height="34" fill="none" stroke="#e9e9e9" stroke-width="3"/><path d="M10 20 L18 28 L31 11" fill="none" stroke="#e9e9e9" stroke-width="4"/></svg>Integrity selling</li>
      <li><svg viewBox="0 0 40 40" aria-hidden="true"><rect x="3" y="3" width="34" height="34" fill="none" stroke="#e9e9e9" stroke-width="3"/><path d="M10 20 L18 28 L31 11" fill="none" stroke="#e9e9e9" stroke-width="4"/></svg>Making a difference</li>
      <li><svg viewBox="0 0 40 40" aria-hidden="true"><rect x="3" y="3" width="34" height="34" fill="none" stroke="#e9e9e9" stroke-width="3"/><path d="M10 20 L18 28 L31 11" fill="none" stroke="#e9e9e9" stroke-width="4"/></svg>Better at communicating</li>
      <li><svg viewBox="0 0 40 40" aria-hidden="true"><rect x="3" y="3" width="34" height="34" fill="none" stroke="#e9e9e9" stroke-width="3"/><path d="M10 20 L18 28 L31 11" fill="none" stroke="#e9e9e9" stroke-width="4"/></svg>More profit</li>
      <li><svg viewBox="0 0 40 40" aria-hidden="true"><rect x="3" y="3" width="34" height="34" fill="none" stroke="#e9e9e9" stroke-width="3"/><path d="M10 20 L18 28 L31 11" fill="none" stroke="#e9e9e9" stroke-width="4"/></svg>Improve relationships</li>
    </ul>
  </section>

  <div class="web-band">
    <svg viewBox="0 0 46 46" aria-hidden="true">
      <g fill="none" stroke="#111" stroke-width="3">
        <circle cx="23" cy="23" r="20"/>
        <ellipse cx="23" cy="23" rx="9" ry="20"/>
        <line x1="3" y1="23" x2="43" y2="23"/>
        <path d="M7 12 H39 M7 34 H39"/>
      </g>
    </svg>
    <span class="web-address">www.brightmolarclinic.com</span>
  </div>
</main>
</body>
</html>
```